Harrow Spirits Bottle Label

BACKGROUND
We are plumbers that have resurrected London's oldest once illicit Gin Distillery KTV Report https://www.vidstream-example.com/watch?v=Qx8rTmL2pWa&t=4s
Bought 150yr old derelict bakery & turned it into an office for our plumbing biz....removed dangerous chimney...got sued by a neighbour ..
our lawyers discovered that the original bakers family once made illict gin here (in what is now our office) we tracked down the origianl family ...see pic enclosed....the little boy now in his 90's (Colin Fenwort) gave us his family's secret gin recipe and we have now resurrected it. We supply Aldermoor Hall, Hse of Elders Pettigrew Hale etc. Now have our 1st Harrow Spirits.
This is NOT scotch whisky...this a brand new category of drink 'English Whisky'
1. traditional whisky style bottle which will have embossed text on as per the sample English Whisky & K T Distillery LONDON
Front label 110mm x 95mm
Rear label 70mm wide and 100mm
Front Text TBC
Rear Text TBC
Must have a old map of my area London Q27 8XZ on rear
Map link https://charts.oldplans-example.org/view-full/558201736#zoom=6&lat=1477&lon=6570&layers=BT

Target Market(s)

OVER 30's

Font styles to use
Sans Serif

Requirements
Nice to have
• I want an old map on the front of the label....the map have 2 small rivers on it which are very close to my distillery (called The Calder Race and Tollet Beck, where they meet there a small bridge called Harecroft Bridge, i would like this shown on the map, is there any tasteful way to add some colour to the historic map ???

```html
<!DOCTYPE html>
<html lang="en">
<head>
<meta charset="utf-8">
<title>Old Granary Whisky – Label</title>
<link rel="stylesheet" href="https://fonts.googleapis.com/css2?family=Playfair+Display:ital,wght@0,400;0,500;0,700;1,400&family=Oswald:wght@500&family=Italianno&family=Poppins:wght@400;600&family=Roboto+Condensed:wght@400&display=swap">
<style>
  :root {
    --paper-front: #ece9e1;
    --paper-back: #e4d8be;
    --ink: #6b3a1c;
    --ink-dark: #4a2a16;
    --ink-soft: #5a3a24;
    --stain: #c9a57a;
    --map-line: #cfcabf;
    --photo-light: #a9a59e;
    --photo-dark: #4e4b46;
    --edge: #9aa0a8;
  }
  * { margin: 0; padding: 0; box-sizing: border-box; }
  html, body { width: 1200px; height: 664px; overflow: hidden; background: #ffffff; }
  .label { position: relative; width: 1200px; height: 664px; overflow: hidden; color: var(--ink); }

  .front-panel {
    position: absolute; left: 0; top: 0; width: 600px; height: 664px;
    background: radial-gradient(ellipse at 8% 50%, rgba(201,165,122,.55) 0, rgba(201,165,122,0) 14%), var(--paper-front);
  }
  .back-panel {
    position: absolute; left: 588px; top: 0; width: 612px; height: 664px;
    background: radial-gradient(ellipse at 95% 10%, rgba(190,165,120,.35), rgba(0,0,0,0) 40%), var(--paper-back);
  }
  .torn-edge { position: absolute; left: 578px; top: 0; width: 24px; height: 664px; }

  .area-map {
    position: absolute; left: 0; top: 70px; width: 590px; height: 240px;
    background: linear-gradient(160deg, rgba(207,202,191,.55), rgba(236,233,225,.2));
  }
  .front-title {
    position: absolute; left: 0; width: 620px; top: 30px; text-align: center;
    font-family: "Playfair Display", serif; font-weight: 700; font-size: 28px;
  }
  .brand-name {
    position: absolute; left: 100px; top: 268px; width: 420px; text-align: center;
    font-family: "Playfair Display", serif; font-weight: 700; font-size: 62px; line-height: 66px;
    color: var(--ink);
  }
  .serve-line {
    position: absolute; left: 0; width: 620px; top: 500px; text-align: center;
    font-family: "Italianno", cursive; font-size: 42px; line-height: 44px;
  }
  .volume {
    position: absolute; left: 0; width: 620px; top: 540px; text-align: center;
    font-family: "Italianno", cursive; font-size: 32px;
  }
  .detail-row {
    position: absolute; left: 174px; top: 598px;
    font-family: "Poppins", sans-serif; font-weight: 600; font-size: 17px;
  }
  .detail-row span { position: absolute; white-space: nowrap; }

  .founder-photo {
    position: absolute; left: 708px; top: 75px; width: 52px; height: 58px;
    background: linear-gradient(180deg, #b8b3a8, #6f6a62);
  }
  .story-intro {
    position: absolute; left: 769px; top: 71px; width: 400px;
    font-family: "Playfair Display", serif; font-size: 13.6px; line-height: 18px; color: var(--ink-dark);
  }
  .section-heading {
    position: absolute; left: 693px; top: 168px; width: 455px; text-align: center;
    font-family: "Oswald", sans-serif; font-weight: 500; font-size: 27px; letter-spacing: 1.2px;
  }
  .history-photo { position: absolute; top: 211px; height: 164px; }
  .history-photo.then { left: 686px; width: 228px; background: linear-gradient(135deg, var(--photo-light), var(--photo-dark)); }
  .history-photo.now { left: 920px; width: 231px; background: linear-gradient(135deg, #8d8880, #5c5852 60%, #a19c94); }

  .story-body {
    position: absolute; left: 686px; top: 392px; width: 466px;
    font-family: "Playfair Display", serif; font-size: 13px; line-height: 16.6px; color: var(--ink-soft);
  }

  .units-box {
    position: absolute; left: 694px; top: 558px; width: 204px; height: 79px;
    border: 2px solid var(--ink-dark); border-radius: 6px;
  }
  .units-box svg { position: absolute; left: 6px; top: 4px; }
  .units-table {
    position: absolute; left: 36px; top: 4px; width: 160px; border-collapse: collapse;
    font-family: "Roboto Condensed", sans-serif; font-size: 8.8px; color: var(--ink-dark);
  }
  .units-table td { border: 1.4px solid var(--ink-dark); padding: 1px 4px; height: 17px; white-space: nowrap; }
  .units-table td.unit-head { line-height: 11px; height: 28px; }
  .units-table td.who { width: 36px; }

  .badge {
    position: absolute; font-family: "Poppins", sans-serif; font-weight: 600; font-size: 6.4px;
    color: var(--ink-dark); text-align: center; line-height: 8px; white-space: nowrap;
  }
  .flag-mark { position: absolute; left: 907px; top: 566px; width: 41px; height: 41px; background: var(--ink-dark); opacity: .85; }
  .web-info {
    position: absolute; left: 1072px; top: 612px; width: 120px; text-align: center; white-space: nowrap;
    font-family: "Poppins", sans-serif; font-weight: 600; font-size: 6.4px; line-height: 9px; color: var(--ink-dark);
  }
</style>
</head>
<body>
<div class="label">
  <section class="front-panel">
    <div class="area-map" role="img" aria-label="Historic map of the local area with two brooks and a small bridge"></div>
    <h1 class="front-title">English Whisky</h1>
    <div class="brand-name">Old<br>Granary<br>Whisky</div>
    <div class="serve-line">As Served in Whitehall</div>
    <div class="volume">50cl</div>
    <div class="detail-row">
      <span style="left:0">batch</span>
      <span style="left:77px">bottle</span>
      <span style="left:156px">artisan</span>
      <span style="left:245px">ABV</span>
    </div>
  </section>

  <svg class="torn-edge" viewBox="0 0 24 664" aria-hidden="true">
    <polyline fill="none" stroke="#9aa0a8" stroke-width="1.6"
      points="12,0 9,30 14,60 8,95 13,130 10,170 15,205 9,240 13,280 8,320 14,355 10,395 15,430 9,470 13,510 8,545 14,585 10,625 13,664"/>
  </svg>

  <section class="back-panel"></section>

  <div class="founder-photo" role="img" aria-label="Portrait photo of the founder"></div>
  <p class="story-intro">Whisky was made in London up until 1905. In 2014 Plumber Ray Tolliver discovered his office (a Bakery over 100yr ago) was location where the Bakers made illicit Gin.</p>

  <h2 class="section-heading">RECREATION OF A HISTORIC PHOTO</h2>
  <div class="history-photo then" role="img" aria-label="Archive street photo of a man on a penny-farthing with a woman and a boy on a tricycle"></div>
  <div class="history-photo now" role="img" aria-label="Recreated street photo of an older man with a penny-farthing and a child on a tricycle"></div>

  <div class="story-body">
    Ray tracked down the Bakers family descendants and got the original illicit Gin recipe &amp; then resurrected it This is a first for English Whisky, handcrafted in London.<br>
    Barley, Wheat Oats from Hartwell Farm 1867 in Norfolk,<br>
    Spirit made in Suffolk in American 40% Toasted Oak Ex Bourbon Casks and aged, matured, finished in 10yr old Cuban Rum Casks in London at London’s oldest once illicit Distillery.<br>
    Non Chill Filtered - No artificial Colour<br>
    Nutty chocolate, caramelised demerara sugar, Toasted Oak, Orange Peel
  </div>

  <div class="units-box">
    <svg width="26" height="70" viewBox="0 0 26 70" aria-hidden="true">
      <path d="M10 2 H16 V16 Q22 20 22 28 V68 H4 V28 Q4 20 10 16 Z" fill="none" stroke="#4a2a16" stroke-width="1.5"/>
      <text x="13" y="47" text-anchor="middle" font-family="Poppins, sans-serif" font-size="10" font-weight="600" fill="#4a2a16">20</text>
      <text x="13" y="56" text-anchor="middle" font-family="Poppins, sans-serif" font-size="6.5" fill="#4a2a16">UK</text>
      <text x="13" y="64" text-anchor="middle" font-family="Poppins, sans-serif" font-size="6.5" fill="#4a2a16">Units</text>
    </svg>
    <table class="units-table">
      <tr><td colspan="2" class="unit-head">UK Chief Medical Officers recommend<br>adults do not regularly exceed</td></tr>
      <tr><td class="who">Men</td><td>3-4 units daily</td></tr>
      <tr><td class="who">Women</td><td>2-3 units daily</td></tr>
    </table>
  </div>

  <div class="flag-mark" role="img" aria-label="National flag"></div>
  <div class="badge" style="left:903px; top:617px; width:50px;">Made in GB</div>

  <svg style="position:absolute; left:980px; top:563px;" width="49" height="49" viewBox="0 0 49 49" aria-hidden="true">
    <circle cx="24.5" cy="24.5" r="22.5" fill="none" stroke="#4a2a16" stroke-width="2.5"/>
    <line x1="8.6" y1="40.4" x2="40.4" y2="8.6" stroke="#4a2a16" stroke-width="2.5"/>
  </svg>
  <div class="badge" style="left:956px; top:617px; width:96px;">avoid alcohol if pregnant<br>or trying to conceive</div>

  <svg style="position:absolute; left:1043px; top:566px;" width="43" height="40" viewBox="0 0 43 40" aria-hidden="true">
    <g fill="none" stroke="#4a2a16" stroke-width="4" stroke-linejoin="round">
      <path d="M14 12 L21.5 3 L28 12"/>
      <path d="M35 20 L39 32 L27 35"/>
      <path d="M16 35 L4 32 L9 20"/>
    </g>
  </svg>

  <div class="web-info">www.oldgranarywhisky-example.com<br>oldgranarywhisky</div>
</div>
</body>
</html>
```